Simple HVAC & Electrical Contractor Billboard

Leasing a 12'3" H by 49'3" W billboard. I'd like to use our current logo and add a few words to let people know what we do. Looking for a clean simple look.
Our company name is Harold Quince Mechanical - What we are is Air Conditioning & Electrical Contractors.

Our license numbers are TACLA00052618K & TECL71204 they will need to be visible on the sign somewhere.

I'm not sure how much information I want to see on the sign. I want to keep it clean but some of our contact info is as follows. Office # 682-540-9263 - Webpage hqmbrixel.com. I feel like most people can search the name to find the contact info they need but I'll defer to the designers to come up with the best design.

I have attached a couple different logos we have used I the past.

```html
<!DOCTYPE html>
<html lang="en">
<head>
<meta charset="utf-8">
<title>Harold Quince Mechanical – Billboard</title>
<link rel="stylesheet" href="https://fonts.googleapis.com/css2?family=Montserrat:wght@500;600&family=Oswald:wght@500;600&display=swap">
<style>
  :root {
    --stage: #4b4b4b;
    --brand-red: #ed1c24;
    --ink: #231f20;
    --paper: #ffffff;
    --band-black: #000000;
    --steel-light: #d9d9d9;
    --steel-dark: #3a3a3a;
  }
  * { box-sizing: border-box; margin: 0; padding: 0; }
  html, body {
    width: 1000px;
    height: 1200px;
    overflow: hidden;
    background: var(--stage);
  }
  .billboard {
    position: absolute;
    left: 40px;
    top: 485px;
    width: 920px;
    height: 230px;
    box-shadow: 0 18px 30px rgba(0,0,0,0.45);
  }
  .billboard__shapes {
    position: absolute;
    inset: 0;
    width: 920px;
    height: 230px;
    display: block;
  }
  .brand {
    position: absolute;
    left: 0;
    top: 0;
    width: 330px;
    height: 230px;
    display: flex;
    flex-direction: column;
    align-items: center;
    justify-content: center;
    gap: 14px;
  }
  .brand__mark {
    width: 54px;
    height: 54px;
    background: var(--brand-red);
  }
  .brand__name {
    font-family: "Montserrat", sans-serif;
    font-weight: 600;
    color: var(--ink);
    text-align: center;
    text-transform: uppercase;
    font-size: 25px;
    line-height: 1.15;
    letter-spacing: 0.5px;
  }
  .headline {
    position: absolute;
    left: 420px;
    width: 480px;
    top: 22px;
    font-family: "Oswald", sans-serif;
    font-weight: 600;
    color: var(--paper);
    text-align: center;
    text-transform: uppercase;
    font-size: 41px;
    line-height: 52px;
    letter-spacing: 0.3px;
    white-space: nowrap;
  }
  .contact {
    position: absolute;
    left: 405px;
    width: 505px;
    top: 138px;
    height: 53px;
    display: flex;
    align-items: center;
    justify-content: center;
    gap: 9px;
    font-family: "Oswald", sans-serif;
    font-weight: 500;
    color: var(--brand-red);
    font-size: 27px;
    line-height: 1;
    white-space: nowrap;
  }
  .contact__icon {
    width: 25px;
    height: 25px;
    flex: none;
  }
  .contact__divider {
    width: 1px;
    height: 28px;
    background: var(--brand-red);
    margin: 0 3px;
    flex: none;
  }
  .licenses {
    position: absolute;
    left: 400px;
    width: 520px;
    top: 191px;
    height: 39px;
    display: flex;
    align-items: center;
    justify-content: center;
    font-family: "Montserrat", sans-serif;
    font-weight: 500;
    color: var(--paper);
    font-size: 12.5px;
    letter-spacing: 0.3px;
    text-transform: uppercase;
    white-space: nowrap;
  }
</style>
</head>
<body>
  <main class="billboard">
    <svg class="billboard__shapes" viewBox="0 0 920 230" aria-hidden="true">
      <defs>
        <linearGradient id="steel-edge" x1="0" y1="0" x2="0" y2="1">
          <stop offset="0" stop-color="#3a3a3a"/>
          <stop offset="0.5" stop-color="#d9d9d9"/>
          <stop offset="1" stop-color="#3a3a3a"/>
        </linearGradient>
      </defs>
      <rect class="band-red" x="0" y="0" width="920" height="138" fill="#ed1c24"/>
      <rect class="band-white" x="0" y="138" width="920" height="53" fill="#ffffff"/>
      <rect class="band-black" x="0" y="191" width="920" height="39" fill="#000000"/>
      <polygon class="chevron-edge" points="311,0 336,0 420,114 336,230 311,230 371,114" fill="url(#steel-edge)"/>
      <polygon class="brand-panel" points="0,0 311,0 371,114 311,230 0,230" fill="#ffffff"/>
    </svg>

    <section class="brand">
      <div class="brand__mark"></div>
      <p class="brand__name">Harold Quince<br>Mechanical</p>
    </section>

    <h1 class="headline">Air Conditioning &amp;<br>Electrical Contractors</h1>

    <section class="contact">
      <svg class="contact__icon" viewBox="0 0 28 28" aria-hidden="true">
        <circle cx="14" cy="14" r="13" fill="#ed1c24"/>
        <circle cx="14" cy="14" r="11" fill="#231f20"/>
        <g fill="none" stroke="#fff" stroke-width="1.2">
          <circle cx="14" cy="14" r="6.5"/>
          <ellipse cx="14" cy="14" rx="3" ry="6.5"/>
          <line x1="7.5" y1="14" x2="20.5" y2="14"/>
          <line x1="8.5" y1="10.5" x2="19.5" y2="10.5"/>
          <line x1="8.5" y1="17.5" x2="19.5" y2="17.5"/>
        </g>
      </svg>
      <span class="contact__web">www.hqmbrixel.com</span>
      <span class="contact__divider"></span>
      <svg class="contact__icon" viewBox="0 0 28 28" aria-hidden="true">
        <circle cx="14" cy="14" r="13" fill="#ed1c24"/>
        <circle cx="14" cy="14" r="11" fill="#231f20"/>
        <path d="M10.2 8.2l2.2-.6 1.3 3.2-1.5 1c.6 1.6 1.6 2.8 3 3.6l1.2-1.4 3 1.5-.7 2.2c-4.5.6-8.9-4.6-8.5-9.5z" fill="#fff"/>
      </svg>
      <span class="contact__phone">682-540-9263</span>
    </section>

    <p class="licenses">License Numbers: TACLA00052618K &amp; TECL71204</p>
  </main>
</body>
</html>
```